Business Card Design for a Sound engineer and DJ

We would like a residn of the business card.

Logo must remain the same.
The card is for the owner of the company.
The business card is in Arabic as the company is based in Kuwait.
The company specializes in sound engineering for singers concerts and events and in addition DJ.
The color options is up to the designer but we would like it masculine as the owner is a man.

Target Market(s)

All ages

Industry/Entity Type

Media

Contact Information for Business Card

Name:
Eng. Faisal Barrak
م/فيصل براك

The name above is in Arabic and English.

Title: General Manager
Mobile: +965 96370482
Office: +965 22480637
Email: info@qamarwave.net

Address:
Office no. 3
1st floor
Marjan Complex
Hamad Faraj St.
Salmiya
Kuwait

Instagram: @qamarwave
Snap: qamarwave

Requirements
Nice to have
• can we have Instagram icon and snap icon and a phone vector and email?
• Instead of writing the words

```html
<!DOCTYPE html>
<html lang="en">
<head>
<meta charset="utf-8">
<title>Qamar Wave – Business Card</title>
<link rel="stylesheet" href="https://fonts.googleapis.com/css2?family=Open+Sans:wght@400;600&family=Cairo:wght@400;600;700&display=swap">
<style>
  :root {
    --stage: #2e3034;
    --card: #ffffff;
    --brand-purple: #7a4aa6;
    --accent-pink: #e2278b;
    --ink: #1b1b1b;
    --ghost: #ececec;
  }
  * { box-sizing: border-box; margin: 0; padding: 0; }
  html, body { width: 1200px; height: 864px; overflow: hidden; }
  body {
    background: var(--stage);
    font-family: "Open Sans", sans-serif;
    position: relative;
  }
  .card {
    position: absolute;
    left: 300px;
    width: 600px;
    height: 343px;
    background: var(--card);
    overflow: hidden;
  }
  .card--front { top: 64px; }
  .card--back { top: 457px; }

  /* front */
  .brand {
    position: absolute;
    inset: 0;
    display: flex;
    flex-direction: column;
    align-items: center;
    justify-content: center;
    color: var(--brand-purple);
  }
  .brand__name-ar {
    font-family: "Cairo", sans-serif;
    font-weight: 700;
    font-size: 74px;
    line-height: 1;
  }
  .brand__name-en {
    font-weight: 600;
    font-size: 30px;
    letter-spacing: 6px;
    text-transform: uppercase;
    margin-top: 10px;
  }
  .brand__services {
    font-weight: 600;
    font-size: 13px;
    letter-spacing: 2px;
    margin-top: 4px;
  }
  .brand__services-ar {
    font-family: "Cairo", sans-serif;
    font-weight: 600;
    font-size: 17px;
    line-height: 1.3;
  }

  /* back */
  .ghost-mark {
    position: absolute;
    left: 150px;
    top: 70px;
    font-family: "Cairo", sans-serif;
    font-weight: 700;
    font-size: 170px;
    line-height: 1;
    color: var(--ghost);
    white-space: nowrap;
  }
  .holder {
    position: absolute;
    top: 30px;
    left: 0;
    right: 0;
    text-align: center;
  }
  .holder__name {
    color: var(--accent-pink);
    font-weight: 600;
    font-size: 21px;
  }
  .holder__name-ar {
    font-family: "Cairo", sans-serif;
    font-size: 15px;
    line-height: 1.2;
    color: var(--ink);
  }
  .holder__title { font-size: 14px; color: var(--ink); }

  .contact {
    position: absolute;
    display: flex;
    align-items: center;
    gap: 8px;
    font-size: 15px;
    color: var(--ink);
  }
  .contact svg { width: 13px; height: 13px; flex: none; }
  .contact--instagram { left: 226px; top: 140px; }
  .contact--snap { left: 346px; top: 160px; }
  .contact--mobile { left: 100px; top: 196px; }
  .contact--office { left: 240px; top: 206px; }
  .contact--email { left: 394px; top: 220px; }

  .address {
    position: absolute;
    left: 70px;
    right: 40px;
    top: 258px;
    font-size: 14.5px;
    line-height: 1.35;
    color: var(--ink);
  }
  .address span { display: block; padding-left: 140px; }
</style>
</head>
<body>

<section class="card card--front">
  <div class="brand">
    <div class="brand__name-ar" lang="ar" dir="rtl">قمر ويف</div>
    <div class="brand__name-en">Qamar Wave</div>
    <div class="brand__services">DJ - SOUND ENG. - LIGHTING</div>
    <div class="brand__services-ar" lang="ar" dir="rtl">دي جي - هندسة صوت - إضاءة</div>
  </div>
</section>

<section class="card card--back">
  <div class="ghost-mark" lang="ar" dir="rtl" aria-hidden="true">قمر ويف</div>

  <div class="holder">
    <div class="holder__name">Eng. Faisal Barrak</div>
    <div class="holder__name-ar" lang="ar" dir="rtl">م/فيصل براك</div>
    <div class="holder__title">General Manager</div>
  </div>

  <div class="contact contact--instagram">
    <svg viewBox="0 0 13 13"><rect width="13" height="13" rx="2" fill="var(--accent-pink)"/></svg>
    <span>@qamarwave</span>
  </div>
  <div class="contact contact--snap">
    <svg viewBox="0 0 13 13"><circle cx="6.5" cy="6.5" r="6.5" fill="var(--accent-pink)"/></svg>
    <span>qamarwave</span>
  </div>
  <div class="contact contact--mobile">
    <svg viewBox="0 0 13 13"><rect x="3" y="0.5" width="7" height="12" rx="1.5" fill="none" stroke="var(--accent-pink)" stroke-width="1.6"/><circle cx="6.5" cy="10" r="0.9" fill="var(--accent-pink)"/></svg>
    <span>+965 96370482</span>
  </div>
  <div class="contact contact--office">
    <svg viewBox="0 0 13 13"><path d="M3 1 L5 1 L6 4 L4.5 5.2 C5.3 7 6 7.7 7.8 8.5 L9 7 L12 8 L12 10 C12 11.2 11 12 9.8 12 C5 11.6 1.4 8 1 3.2 C1 2 1.8 1 3 1 Z" fill="var(--accent-pink)"/></svg>
    <span>+965 22480637</span>
  </div>
  <div class="contact contact--email">
    <svg viewBox="0 0 13 13"><rect x="0.5" y="2.5" width="12" height="8" rx="1" fill="var(--accent-pink)"/><path d="M1 3 L6.5 7 L12 3" fill="none" stroke="#fff" stroke-width="1"/></svg>
    <span>info@qamarwave.net</span>
  </div>

  <address class="address" style="font-style:normal">
    Office no. 3 1st floor Marjan Complex Hamad Faraj St.
    <span>Salmiya Kuwait</span>
  </address>
</section>

</body>
</html>
```